CalmPeak Nurses' Manifesto

Design a manifesto to inspire and motivate nurses to work at minimum standards of excellence in their nursing practice.

The manifesto will become a feature of our website, at conferences, workshops and retreats. It will also be featured on other marketing tools.

Primary Market:
Nurses and/or other healthcare professionals (specifically Doctors, Occupational Therapists, Psychologists and Social Workers).

However the manifesto is equally applicable to all nurses and healthcare professionals from new graduates to very experienced senior clinicians, administration officers,managers and healthcare executive personnel.

Mainly females and primarily 35 to 65 years old, which suggests people in this target age group have extensive experience, but have become jaded'.

The purpose of our business is to assist healthcare professionals, primarily nurses, to maintain their enthusiasm and excellence in service provision, for their benefit as well as the benefit of the clients.

I have attached:
File 1: Copy Samples and examples: which has the copy for the manifesto, examples that appeal to us and our 3 attempts.
File 2: Our colour Spec Sheet, HOWEVER the colours are not necessary limited to these colours. These colours are not in the logo that will be on the manifesto. The colours on the logo attached can/or also be used.
File 3: Prototype logo. The final logo will be available within 3 to 4 days.

Industry/Entity Type

Healthcare

Requirements
Must have
• Must use the copy as per the attached file.

It should be contemporary, eye catching and motivational.

Should not have
• MUST BE EASY TO READ. Each line MUST be clearly defined from each other.

```html
<!DOCTYPE html>
<html lang="en">
<head>
<meta charset="utf-8">
<title>CalmPeak Nurses' Manifesto</title>
<link href="https://fonts.googleapis.com/css2?family=Open+Sans:ital,wght@0,400;0,700;0,800;1,700&display=swap" rel="stylesheet">
<style>
:root{
  --sky:#3b8fe8;
  --ocean:#1f5fa8;
  --azure:#2b8bdb;
  --magenta:#e62eb8;
  --pink:#ec3cc8;
  --orange:#f05a14;
  --gold:#8b6a14;
  --umber:#5a4620;
  --navy:#1a2f9a;
  --lime:#5ad22a;
  --slate:#5a6063;
  --red:#e8141e;
  --royal:#1f6fc0;
  --violet:#7a3ee0;
  --rust:#8a4a14;
  --leaf:#2a8a3a;
  --ink:#111;
  --paper:#fff;
}
*{margin:0;padding:0;box-sizing:border-box}
html,body{width:900px;height:1200px;overflow:hidden;background:var(--paper)}
body{font-family:"Open Sans",Arial,sans-serif}
.manifesto{position:relative;width:900px;height:1200px;overflow:hidden;background:var(--paper)}
.block{position:absolute;font-size:24px;line-height:1.5}
.key{font-weight:700;letter-spacing:-.5px}
.just{text-align:justify;text-align-last:justify}
.band{position:absolute;background:var(--sky)}
.band--top-left{left:48px;top:0;width:28px;height:14px}
.band--top-right{left:580px;top:0;width:300px;height:14px}
.band--bottom-left{left:48px;top:1140px;width:28px;height:60px}
.dream-bar{position:absolute;left:490px;top:1140px;width:390px;height:60px;background:var(--sky);color:#fff;font-size:26px;display:flex;align-items:center;justify-content:center;gap:8px}
.dream-bar strong{font-size:36px;font-weight:800}

.title{left:62px;top:14px;font-size:60px;color:var(--sky);font-weight:400;line-height:1.2}
.deliver{left:660px;top:28px;color:var(--ocean);font-size:24px;line-height:1.3}
.deliver .key{font-size:36px}
.nurse{left:40px;top:98px;color:var(--gold);font-size:25px}
.nurse .key{font-size:38px}
.learn{left:590px;top:100px;width:272px;text-align:right;color:var(--magenta);font-size:25px;line-height:1.4}
.learn .key{font-size:40px}
.self-care{left:40px;top:152px;width:275px;color:var(--ink);font-size:24.5px;line-height:1.48}
.be{left:40px;top:298px;color:var(--magenta);font-size:24px}
.be .key{font-size:40px}
.respond{left:336px;top:152px;width:290px;color:var(--azure);font-size:24.5px;line-height:1.48}
.respond .key{font-size:38px;line-height:1}
.celebrate{left:636px;top:206px;width:230px;text-align:center;color:var(--orange);font-size:22px;line-height:1.3}
.celebrate .key{font-size:42px}
.celebrate em{font-weight:700;font-size:25px}
.celebrate .culture{display:block;font-size:36px;font-weight:700;line-height:1.2;margin-top:16px}
.respect{left:40px;top:352px;width:580px;color:var(--umber);font-size:25px;line-height:1.45}
.respect .key{font-size:40px;color:#5a4010;line-height:1}
.smile{left:40px;top:444px;width:410px;color:var(--navy);font-size:25px;line-height:1.45}
.smile .key{font-size:38px;line-height:1}
.seek{left:40px;top:522px;color:var(--lime);font-size:25px}
.seek .key{font-size:40px}
.trust{left:535px;top:450px;width:325px;color:var(--magenta);font-size:25px;line-height:1.45}
.trust .key{font-size:40px;line-height:1}
.adapt{left:40px;top:576px;color:var(--sky);font-size:25px}
.adapt .key{font-size:40px}
.choose{left:42px;top:636px;width:275px;color:var(--slate);font-size:25px;line-height:1.45}
.choose .key{font-size:40px;line-height:1}
.support{left:355px;top:634px;width:220px;text-align:center;color:var(--red);font-size:25px;line-height:1.45}
.support .key{font-size:40px;line-height:1}
.you{left:628px;top:634px;width:240px;color:var(--slate);font-size:25px;line-height:1.45}
.you .key{font-size:40px;line-height:1}
.solution{left:42px;top:780px;color:var(--pink);font-size:25px;line-height:1.45}
.solution .key{font-size:40px;line-height:1}
.delight{left:322px;top:808px;width:540px;color:var(--royal);font-size:25px;line-height:1.45}
.delight .key{font-size:40px;line-height:1}
.delight em{font-weight:700}
.right-thing{left:44px;top:878px;color:var(--ink);font-size:25px;line-height:1.45}
.right-thing .key{font-size:40px;line-height:1}
.lead-on{left:510px;top:914px;width:312px;color:var(--sky);font-size:25px;line-height:1.45}
.lead-on .key{display:block;text-align:right;font-size:38px;line-height:1.1;color:var(--royal)}
.follow{left:40px;top:976px;color:var(--violet);font-size:25px}
.follow .key{font-size:40px}
.purpose{left:40px;top:1030px;color:var(--rust);font-size:25px;line-height:1.5}
.purpose .key{font-size:40px}
.purpose em{font-weight:700}
.purpose .indent{padding-left:138px}

.brand{position:absolute;display:flex;align-items:center;gap:10px}
.brand--program{left:600px;top:1060px;font-size:30px;font-weight:700;color:var(--leaf)}
.brand--program .dot{width:26px;height:26px;border-radius:50%;background:var(--orange)}
.brand--partner{left:78px;top:1122px;font-size:21px;color:var(--leaf)}
.brand--partner .square{width:30px;height:30px;background:var(--lime)}
</style>
</head>
<body>
<main class="manifesto">
  <div class="band band--top-left"></div>
  <div class="band band--top-right"></div>

  <h1 class="block title">Nurses' Manifesto</h1>
  <p class="block deliver">Deliver<br><span class="key">care</span> skillfully.</p>

  <p class="block nurse"><span class="key">Nurse</span> with open hands, hearts and</p>
  <p class="block learn"><span class="key">Learn</span> &nbsp;something new each day.</p>

  <p class="block self-care just">Look after yourself and value your health as much as you value the health of others.</p>
  <p class="block be"><span class="key">Be</span> a lifelong learner.</p>

  <p class="block respond"><span class="key">Respond</span> to complex situations innovatively, creatively and safely within the scope of your practice.</p>

  <p class="block celebrate"><span class="key">Celebrate</span>,<br><em>respect</em> and <em>value</em><br>the diversity of<span class="culture">Australian culture.</span></p>

  <p class="block respect just"><span class="key">Respect</span> the limits of people's knowledge and share your knowledge generously.</p>

  <p class="block smile"><span class="key">Smile</span> and infect others with your happiness and have fun!</p>
  <p class="block seek"><span class="key">Seek</span> success firstly from within.</p>
  <p class="block trust just"><span class="key">Trust</span> your knowledge and seek <strong>advice</strong> only from respected sources.</p>

  <p class="block adapt"><span class="key">Adapt</span> a ‘<strong><em>can do</em></strong>’ attitude to everything that comes your way.</p>

  <p class="block choose"><span class="key">Choose</span> your thoughts wisely, they create your reality.</p>
  <p class="block support"><span class="key">Support</span><br>your colleagues and champion their purpose.</p>
  <p class="block you"><span class="key">You</span> are<br>unique, revel in<br>&nbsp;your individuality.</p>

  <p class="block solution"><span class="key">Always</span> be<br>solution focused.</p>
  <p class="block delight"><span class="key">Delight</span> your <em>clients</em> and <em>colleagues</em> by exceeding their expectations.</p>

  <p class="block right-thing"><span class="key">Always</span> do<br>the right thing without exception.</p>
  <p class="block lead-on">If there is no one left to follow, then <span class="key">lead!</span></p>

  <p class="block follow">Only <span class="key">follow</span> exceptional leaders.</p>
  <p class="block purpose">Always <span class="key">lead</span> with <em>purpose</em>,<br><span class="indent"><em>passion</em> and <em>commitment</em>.</span></p>

  <div class="brand brand--program"><span class="dot"></span>CalmPeak For Nurses</div>
  <div class="brand brand--partner"><span class="square"></span>Care Growth Partners</div>

  <div class="band band--bottom-left"></div>
  <div class="dream-bar">Live your <strong>dream</strong> .</div>
</main>
</body>
</html>
```